Boutique Technology Consultancy specialising is Electronic and physical security

We need to redo our existing outdated website. For your reference the link www.pelu.com.au

```html
<!DOCTYPE html>
<html lang="en">
<head>
<meta charset="utf-8">
<title>Pelu Services</title>
<link href="https://fonts.googleapis.com/css2?family=Lato:wght@400;700;900&display=swap" rel="stylesheet">
<style>
:root{
  --red:#9e2428;
  --red-dark:#7f1b1f;
  --pink:#f4e3e4;
  --pink-soft:#f8eeee;
  --ink:#1c1c1c;
  --text:#444;
  --white:#fff;
  --grey-bg:#ececec;
  --footer:#2b2b2b;
  --black:#0d0d0d;
}
*{box-sizing:border-box;margin:0;padding:0}
html,body{width:1200px;height:3720px;overflow:hidden}
body{font-family:'Lato',sans-serif;color:var(--text);background:var(--white);position:relative}
.abs{position:absolute}
.btn{position:absolute;background:var(--red);color:var(--white);font-size:14px;display:flex;align-items:center;justify-content:center;border-radius:2px}

/* hero */
.hero{position:absolute;left:0;top:0;width:1200px;height:582px;background:linear-gradient(160deg,#2f4a63 0%,#4f6b84 40%,#2a4058 75%,#1d3045 100%)}
.logo{position:absolute;color:var(--white);font-weight:700;letter-spacing:1px;display:flex;align-items:center;gap:10px}
.logo .mark{width:18px;height:18px;background:var(--red)}
.nav{position:absolute;top:24px;left:604px;display:flex;gap:0;color:var(--white);font-size:15px}
.nav span{position:absolute;white-space:nowrap}
.quick{position:absolute;left:1014px;top:16px;color:var(--white);font-size:13px;line-height:1.3}
.quick b{display:block;font-size:16px;font-weight:400;letter-spacing:1px}
.hero-title{position:absolute;left:84px;top:278px;color:var(--white);font-weight:700;font-size:50px;line-height:80px}
.hero-title .hl{border:3px solid var(--white);background:var(--red);padding:0 8px;line-height:56px;display:inline-block}

/* about */
.about-band{position:absolute;left:0;top:582px;width:380px;height:541px;background:var(--red);border-bottom-right-radius:40px}
.about-shadow{position:absolute;left:380px;top:694px;width:775px;height:420px;background:var(--pink-soft)}
.about-card{position:absolute;left:168px;top:667px;width:970px;height:420px;background:var(--white);border-radius:22px 0 0 22px;padding:22px 22px 0 22px;font-size:14.5px;line-height:23px}
.about-title{position:absolute;left:188px;top:612px;color:var(--white);font-size:36px;font-weight:700}
.about-card p{margin-bottom:10px}
.about-card ul{list-style:none;margin-bottom:10px}
.about-card li:before{content:"\203A\00a0"}

/* services */
.svc-intro{position:absolute;left:69px;top:1207px;width:510px;font-size:14px;line-height:21px}
.pill{position:absolute;left:62px;height:31px;background:var(--red);color:var(--white);font-weight:700;font-size:16px;padding:0 20px;border-radius:0 16px 16px 0;display:flex;align-items:center}
.svc-items{position:absolute;left:82px;width:500px;font-size:13px;line-height:20px}
.svc-items span{margin-right:12px;white-space:nowrap}
.svc-items span:before{content:"\203A\00a0"}
.svc-photo{position:absolute;left:598px;top:1190px;width:540px;height:387px;background:linear-gradient(135deg,#8d8d8d,#3b3b3b 55%,#b9b9b9)}
.svc-label-bg{position:absolute;left:553px;top:1530px;width:200px;height:74px;background:var(--pink)}
.svc-label{position:absolute;left:565px;top:1516px;width:200px;height:74px;background:var(--red);color:var(--white);font-size:34px;font-weight:700;display:flex;align-items:center;justify-content:center;border-radius:4px}

/* experience */
.h2{position:absolute;font-size:36px;font-weight:700;color:var(--ink)}
.exp-intro{position:absolute;left:74px;top:1746px;width:1060px;font-size:14px;line-height:21px}
.exp-card{position:absolute;top:1814px;width:258px;height:286px;background:var(--pink-soft)}
.exp-card .img{height:173px;background:linear-gradient(160deg,#d7d7d7,#6c6c6c)}
.exp-card .go{position:absolute;right:12px;top:158px;width:32px;height:32px;border-radius:50%;background:var(--red)}
.exp-card h3{margin:14px 0 4px 8px;font-size:15px;color:var(--ink);font-weight:700}
.exp-card p{margin:0 14px 0 8px;font-size:11px;line-height:15px}
.see-more{left:543px;top:2137px;width:114px;height:35px;font-weight:700;border-radius:4px}

/* team */
.team{position:absolute;left:0;top:2224px;width:1200px;height:505px;background:linear-gradient(135deg,#1c1c1c,#050505 50%,#1a1a1a)}
.team-title{position:absolute;left:0;width:1200px;top:2262px;text-align:center;color:var(--white);font-size:36px;font-weight:700}
.tcard{position:absolute;top:2338px;width:339px;height:313px;background:var(--white);overflow:hidden}
.tcard .arc{position:absolute;right:-20px;top:-100px;width:180px;height:180px;border-radius:50%;background:var(--pink)}
.tcard .arc2{position:absolute;right:12px;top:-72px;width:120px;height:120px;border-radius:50%;background:#e6b9bb}
.tcard .ring{position:absolute;right:38px;top:20px;width:56px;height:56px;border-radius:50%;border:3px solid var(--red)}
.tcard .photo{position:absolute;left:12px;top:14px;width:136px;height:136px;border-radius:50%;background:radial-gradient(circle at 50% 40%,#d8b9a5,#6a5a50)}
.tcard h3{position:absolute;left:12px;top:195px;font-size:17.5px;color:var(--ink);font-weight:700}
.tcard p{position:absolute;left:12px;top:226px;width:315px;height:34px;overflow:hidden;font-size:12.5px;line-height:17px;color:var(--ink)}
.tcard .btn{left:14px;top:270px;width:92px;height:29px;font-size:12.5px}
.arrow{position:absolute;top:2676px;width:32px;height:32px;background:var(--red)}

/* contact */
.contact{position:absolute;left:0;top:2729px;width:1200px;height:784px;background:var(--grey-bg)}
.form{position:absolute;left:62px;top:2825px;width:518px;height:593px;background:#e2e4e7}
.eyebrow{position:absolute;left:84px;top:2852px;font-size:15px;color:var(--ink)}
.eyebrow:before{content:"";display:inline-block;width:12px;height:3px;background:var(--red);vertical-align:middle;margin-right:8px}
.field-label{position:absolute;left:89px;font-size:14.5px;color:var(--text)}
.field{position:absolute;left:85px;width:474px;height:43px;background:var(--white)}
.offices{position:absolute;left:602px;top:2825px;width:536px;height:593px;background:#efd5d7}
.office h4{position:absolute;left:628px;color:var(--red);font-size:15.5px;font-weight:700}
.office p{position:absolute;left:628px;font-size:13.5px;line-height:23px;color:var(--text)}
.map{position:absolute;left:824px;width:292px;height:130px;background:linear-gradient(135deg,#3a3a3a,#1f1f1f)}
.licence{position:absolute;left:628px;top:3372px;font-size:13.5px;color:var(--ink)}

/* footer */
.footer{position:absolute;left:0;top:3513px;width:1200px;height:207px;background:var(--footer);color:var(--white)}
.fhead{position:absolute;font-size:16px;font-weight:700;color:var(--white)}
.flink{position:absolute;font-size:12px;color:#ddd;white-space:nowrap}
.fbottom{position:absolute;left:0;top:3699px;width:1200px;height:21px;background:#1f1f1f;font-size:9px;color:#bbb}
</style>
</head>
<body>

<!-- hero -->
<section class="hero" role="img" aria-label="Glass office tower facade with a security camera"></section>
<div class="logo" style="left:65px;top:14px;font-size:38px"><span class="mark"></span>PELU</div>
<nav class="nav">
  <span style="left:0">About</span>
  <span style="left:71px">Team</span>
  <span style="left:138px">Services</span>
  <span style="left:226px">Experience</span>
  <span style="left:327px">Contact</span>
</nav>
<div class="quick">Quick Contact<b>1300 000 199</b></div>
<h1 class="hero-title">YOUR <span class="hl">TECHNOLOGY</span><br>PROJECTS MADE EASY.</h1>

<!-- about -->
<div class="about-band"></div>
<div class="about-shadow"></div>
<h2 class="about-title">ABOUT</h2>
<div class="about-card">
  <p>Pelu Services was established in 2016 by Ben Ferris to provide technology consulting services to corporate and government clients with a focus on:</p>
  <ul><li>Property/facilities management</li><li>Asset management</li><li>Development and Construction</li></ul>
  <p>In 2022, Pelu Services merged Kestrel Group into its operations, bringing increased capacity and capability to the NSW office.<br>Pelu is a privately owned independent consultancy 100% dedicated to customer satisfaction. With experience in a range of technologies such as internet of things, security systems, wi-fi, building services networks, control centres and smart buildings, our services include:</p>
  <ul style="margin-top:14px;line-height:22px"><li>Technology audits</li><li>Technology roadmaps</li><li>Technology designs</li><li>Technology procurement</li><li>Technology project management</li></ul>
</div>
<div class="btn" style="left:189px;top:1029px;width:103px;height:34px">Read More&nbsp;›</div>

<!-- services -->
<p class="svc-intro">Pelu Services provides independent professional services for projects as well as operations and maintenance. We offer end to end services including:</p>
<div class="pill" style="top:1256px">Strategy</div>
<div class="svc-items" style="top:1301px"><span>Technology roadmaps;</span><span>Master standards; and</span><span>Asset management plans.</span></div>
<div class="pill" style="top:1339px">Projects:</div>
<div class="svc-items" style="top:1383px"><span>Audit;</span><span>Design;</span><span>Procurement;</span><span>Technical project management; and</span><br><span>Witness testing.</span></div>
<div class="pill" style="top:1434px">Operations and maintenance</div>
<div class="svc-items" style="top:1479px"><span>Service and maintenance specifications;</span><span>Policies and procedures;</span><br><span>Procurement; and</span><span>Service reviews.</span></div>
<div class="btn" style="left:71px;top:1529px;width:102px;height:35px">Read More&nbsp;›</div>
<div class="svc-photo" role="img" aria-label="Server racks with patch cabling"></div>
<div class="svc-label-bg"></div>
<div class="svc-label">SERVICES</div>

<!-- experience -->
<h2 class="h2" style="left:72px;top:1692px">EXPERIENCE</h2>
<p class="exp-intro">Pelu has a diverse range of project experience across a range of industries within both the public and private sectors. The following is a small sample of some of the clients and sites we have worked with.</p>
<article class="exp-card" style="left:62px"><div class="img" role="img" aria-label="Shopping centre glass dome"></div><span class="go"></span><h3>City Central</h3><p>Security technology design consulting for this popular retail and entertainment hub which is managed by the Atlas Group.</p></article>
<article class="exp-card" style="left:335px"><div class="img" role="img" aria-label="Motorway with gantries"></div><span class="go"></span><h3>Metro Link</h3><p>Virtual servers, network and CCTV upgrade design and project management for this landmark road transportation Public Private Partnership (PPP).</p></article>
<article class="exp-card" style="left:608px"><div class="img" role="img" aria-label="Hospital building exterior"></div><span class="go"></span><h3>Parkside Women's Hospital</h3><p>Security technology lifecycle consulting for this leading Health Care Public Private Partnership (PPP) which is operated by Harbour &amp; Vale.</p></article>
<article class="exp-card" style="left:880px"><div class="img" role="img" aria-label="Office tower skyline"></div><span class="go"></span><h3>Meridian Towers</h3><p>Shared building network and security systems integration consulting for this iconic office tower which is managed by Crestline.</p></article>
<div class="btn see-more">SEE MORE</div>

<!-- team -->
<section class="team" role="img" aria-label="Dark triangular pattern background"></section>
<h2 class="team-title">OUR TEAM</h2>
<article class="tcard" style="left:62px"><span class="arc"></span><span class="arc2"></span><span class="ring"></span><div class="photo" role="img" aria-label="Portrait of Ben Ferris"></div><h3>Ben Ferris - Principal Consultant</h3><p>Ben founded Pelu in 2016 and continues to lead the organisation nationally.</p><span class="btn">Read More</span></article>
<article class="tcard" style="left:430px"><span class="arc"></span><span class="arc2"></span><span class="ring"></span><div class="photo" role="img" aria-label="Portrait of Simon Marsh"></div><h3>Simon Marsh - Principal Consultant</h3><p>Simon founded Kestrel Group in 2016 and joined Pelu as a Director in 2022, taking over leadership of the NSW office.</p><span class="btn">Read More</span></article>
<article class="tcard" style="left:797px"><span class="arc"></span><span class="arc2"></span><span class="ring"></span><div class="photo" role="img" aria-label="Portrait of Daniel Garner"></div><h3>Daniel Garner - Senior Consultant</h3><p>Daniel established Pelu's Queensland office in 2019 and leads all of Pelu's engagements in the northern states.</p><span class="btn">Read More</span></article>
<svg class="arrow" style="left:562px" viewBox="0 0 32 32"><path d="M19 9l-7 7 7 7" fill="none" stroke="#fff" stroke-width="3"/></svg>
<svg class="arrow" style="left:607px" viewBox="0 0 32 32"><path d="M13 9l7 7-7 7" fill="none" stroke="#fff" stroke-width="3"/></svg>

<!-- contact -->
<section class="contact"></section>
<div class="form"></div>
<div class="eyebrow">Get In Touch</div>
<h2 class="h2" style="left:84px;top:2880px">CONTACT</h2>
<span class="field-label" style="top:2938px">Name</span><div class="field" style="top:2967px"></div>
<span class="field-label" style="top:3026px">Email</span><div class="field" style="top:3055px"></div>
<span class="field-label" style="top:3114px">Subject</span><div class="field" style="top:3143px"></div>
<span class="field-label" style="top:3202px">Message</span><div class="field" style="top:3233px;height:92px"></div>
<div class="btn" style="left:86px;top:3355px;width:110px;height:38px;font-size:15px">Submit Query</div>

<div class="offices"></div>
<div class="office">
  <h4 style="top:2858px">Melbourne Office</h4>
  <p style="top:2888px">Ben Ferris<br>0400 000 111</p>
  <p style="top:2940px">Level 2, 120 Example St,<br>Melbourne VIC 3000</p>
  <div class="map" style="top:2862px" role="img" aria-label="Map of Melbourne office location"></div>
  <h4 style="top:3028px">Queensland Office</h4>
  <p style="top:3058px">Daniel Garner<br>0400 000 222</p>
  <p style="top:3110px">15 Sample Street,<br>Brisbane QLD 4000</p>
  <div class="map" style="top:3032px" role="img" aria-label="Map of Brisbane office location"></div>
  <h4 style="top:3198px">Sydney Office</h4>
  <p style="top:3228px">Tim Salter<br>0400 000 333</p>
  <p style="top:3280px">8 Harbour Lane,<br>Sydney NSW 2000</p>
  <div class="map" style="top:3202px" role="img" aria-label="Map of Sydney office location"></div>
</div>
<p class="licence">New South Wales Master Security Licence Number: <b>000123456</b></p>

<!-- footer -->
<footer class="footer"></footer>
<div class="logo" style="left:70px;top:3566px;font-size:44px"><span class="mark"></span>PELU</div>
<span class="fhead" style="left:303px;top:3540px">Quick Links</span>
<span class="flink" style="left:303px;top:3584px">About</span>
<span class="flink" style="left:371px;top:3584px">Team</span>
<span class="flink" style="left:439px;top:3584px">Services</span>
<span class="flink" style="left:303px;top:3614px">Experience</span>
<span class="flink" style="left:381px;top:3614px">Contact</span>
<span class="fhead" style="left:542px;top:3540px">Services</span>
<span class="flink" style="left:542px;top:3584px">Smart Buildings</span>
<span class="flink" style="left:654px;top:3584px">Systems Integration</span>
<span class="flink" style="left:794px;top:3584px">Control Centres</span>
<span class="flink" style="left:924px;top:3584px">CCTV</span>
<span class="flink" style="left:996px;top:3584px">Access Control</span>
<span class="flink" style="left:542px;top:3614px">Smart Cards</span>
<span class="flink" style="left:654px;top:3614px">Electronic Lockers</span>
<span class="flink" style="left:789px;top:3614px">Intruder Alarms</span>
<span class="flink" style="left:906px;top:3614px">Staff Safety Alarms</span>
<span class="flink" style="left:1041px;top:3614px">Retail Analytics</span>
<span class="flink" style="left:542px;top:3644px">Intercoms</span>
<span class="flink" style="left:637px;top:3644px">Internet of Things</span>
<span class="flink" style="left:759px;top:3644px">Networks</span>
<span class="flink" style="left:857px;top:3644px">Wi-Fi</span>
<div class="fbottom"><span class="abs" style="left:62px;top:5px">Pelu Services Pty Ltd</span><span class="abs" style="right:62px;top:5px">ABN: 00 000 000 000</span></div>

</body>
</html>
```